Interior Stylist business card design needed

I need a business card for my new company in Sydney called "Lu Brannigan Designs". The business offers an interior styling and colour consultancy. My clients are generally not very design savvy (hence why they use me) and can range from being quite conservative to really wanting something "out there". They can be looking for a budget makeover or something more expensive / substantial. I'd like my business card design to be stylish (but not overly formal). I certainly don't want it to be conservative. I'd like it to stand out a bit! I don't really have any aversion to particular colours and I don't have a logo as such - my business name is really all I have.

Target Market(s)

As above - home owners, ranging from conservative to modern

Industry/Entity Type

Conservative

Contact Information for Business Card

Lu Brannigan Designs
Colour consultancy and interior styling
ph: 0417 368 205
email: lubrannigan@zephmail.net.au

Requirements
Should not have
• Old fashioned writing or motifs. No Times Roman font!!

```html
<!DOCTYPE html>
<html lang="en">
<head>
<meta charset="utf-8">
<title>Lu Brannigan Designs – Business Card</title>
<link rel="stylesheet" href="https://fonts.googleapis.com/css2?family=Cormorant+Garamond:ital,wght@0,500;1,500&family=Pinyon+Script&display=swap">
<style>
  :root {
    --backdrop: #2b221d;
    --card: #050505;
    --silver: #d9d9d9;
    --silver-light: #f2f2f2;
    --silver-dark: #9d9d9d;
    --ornament-a: #b8b8b8;
    --ornament-b: #6e6e6e;
    --ink: #111111;
  }
  * { box-sizing: border-box; margin: 0; padding: 0; }
  html, body {
    width: 1200px; height: 900px; overflow: hidden;
    background: var(--backdrop);
  }
  .canvas { position: relative; width: 1200px; height: 900px; }

  .card {
    position: absolute;
    width: 560px; height: 320px;
    background: var(--card);
    border-radius: 26px;
    overflow: hidden;
    box-shadow: 0 14px 30px rgba(0,0,0,.45);
  }
  .card--front { left: 90px; top: 90px; }
  .card--back  { left: 550px; top: 490px; }

  .ornament {
    position: absolute;
    border-radius: 40% 40% 40% 40% / 60% 60% 60% 60%;
    background: linear-gradient(90deg, transparent 0%, var(--ornament-b) 15%, var(--ornament-a) 50%, var(--ornament-b) 85%, transparent 100%);
    opacity: .8;
  }

  .wordmark {
    position: absolute;
    text-align: center;
    color: var(--silver-light);
    font-family: "Cormorant Garamond", serif;
    font-weight: 500;
    line-height: 1;
  }
  .wordmark__name { display: block; }
  .wordmark__suffix { display: block; letter-spacing: .18em; text-transform: uppercase; }

  /* front */
  .card--front .ornament--top    { left: 170px; top: 58px; width: 240px; height: 46px; }
  .card--front .ornament--bottom { left: 150px; top: 222px; width: 260px; height: 46px; }
  .card--front .wordmark { left: 0; right: 0; top: 116px; }
  .card--front .wordmark__name { font-size: 54px; }
  .card--front .wordmark__suffix { font-size: 24px; margin-top: 8px; }

  /* back */
  .tagline {
    position: absolute; left: 34px; top: 38px;
    font-family: "Pinyon Script", cursive;
    font-size: 24px; color: var(--silver-light);
  }
  .card--back .ornament--top    { left: 300px; top: 74px; width: 170px; height: 28px; }
  .card--back .ornament--bottom { left: 310px; top: 168px; width: 180px; height: 30px; }
  .card--back .wordmark { left: 260px; width: 260px; top: 106px; }
  .card--back .wordmark__name { font-size: 32px; }
  .card--back .wordmark__suffix { font-size: 15px; margin-top: 5px; }

  .contact-band {
    position: absolute; left: 0; right: 0; top: 214px; height: 56px;
    background: linear-gradient(180deg, var(--silver-light) 0%, var(--silver) 55%, var(--silver-dark) 100%);
    display: flex; align-items: center; justify-content: space-between;
    padding: 0 36px;
    font-family: "Cormorant Garamond", serif;
    font-style: italic; font-weight: 500;
    font-size: 21px; color: var(--ink);
  }
  .contact-item { display: flex; align-items: center; gap: 12px; }
  .contact-icon { width: 16px; height: 16px; flex: none; }
</style>
</head>
<body>
<main class="canvas">

  <section class="card card--front" aria-label="Business card front">
    <div class="ornament ornament--top" role="img" aria-label="Silver baroque flourish ornament"></div>
    <h1 class="wordmark">
      <span class="wordmark__name">Lu Brannigan</span>
      <span class="wordmark__suffix">Designs</span>
    </h1>
    <div class="ornament ornament--bottom" role="img" aria-label="Silver baroque flourish ornament"></div>
  </section>

  <section class="card card--back" aria-label="Business card back">
    <p class="tagline">Colour consultancy and interior styling</p>
    <div class="ornament ornament--top" role="img" aria-label="Silver baroque flourish ornament"></div>
    <h2 class="wordmark">
      <span class="wordmark__name">Lu Brannigan</span>
      <span class="wordmark__suffix">Designs</span>
    </h2>
    <div class="ornament ornament--bottom" role="img" aria-label="Silver baroque flourish ornament"></div>

    <div class="contact-band">
      <span class="contact-item">
        <svg class="contact-icon" viewBox="0 0 16 16" aria-hidden="true">
          <circle cx="8" cy="8" r="7" fill="none" stroke="#111" stroke-width="1.2"/>
          <path d="M5.4 4.6c.4-.4.9-.4 1.1 0l.6 1.1c.2.3.1.7-.2.9l-.4.3c.4.9 1.1 1.6 2 2l.3-.4c.2-.3.6-.4.9-.2l1.1.6c.4.2.4.7 0 1.1-.7.7-1.6.8-2.6.3-1.3-.7-2.4-1.8-3.1-3.1-.5-1-.4-1.9.3-2.6z" fill="#111"/>
        </svg>
        0417 368 205
      </span>
      <span class="contact-item">
        <span aria-hidden="true">@</span>
        lubrannigan@zephmail.net.au
      </span>
    </div>
  </section>

</main>
</body>
</html>
```